New Logo, New Business Cards! Looking for Refresh

We're in the process of modernizing our entire organization, and with that came the redesign of our logo (attached). We're looking for a designer to develop our new business cards.
Looking for a design that will bring the company in 2020 and help showcase our new logo. Work with the colors of the logo. Feel free to experiment with the logo in white or black if you want. Both now attached.
Industry/Entity Type
Non Profit
Contact Information for Business Card
Address:
48315 Brackwell Avenue, Suite 512
Richmond Hill, ON, L7R 5K2
Name: Marcus Delvecki, MBA
Position: Executive Director
Telephone: 905-362-7048, Ext. 218
Cell Phone: 416-573-2046
Email: marcus@quorvel.ca
Website: www.quorvel.ca
Look and feel
Each slider illustrates characteristics of the customer's brand and the style your logo design should communicate.

```html
<!DOCTYPE html>
<html lang="en">
<head>
<meta charset="utf-8">
<title>Quorvel Business Cards</title>
<link rel="stylesheet" href="https://fonts.googleapis.com/css2?family=Fjalla+One&family=Roboto:wght@400;700&display=swap">
<style>
  :root {
    --bg: #ececec;
    --green-dark: #0b5a26;
    --green-mid: #2f8c34;
    --green-light: #4a9d3e;
    --green-deep: #0e4a22;
    --paper: #f8f8f6;
    --ink: #333333;
  }
  * { box-sizing: border-box; margin: 0; padding: 0; }
  html, body { width: 1200px; height: 852px; overflow: hidden; }
  body {
    background: var(--bg);
    font-family: "Roboto", Arial, sans-serif;
    position: relative;
  }
  .card {
    position: absolute;
    top: 281px;
    width: 500px;
    height: 290px;
    border-radius: 22px;
    box-shadow: 0 4px 14px rgba(0,0,0,0.18);
    overflow: hidden;
  }
  .card--front {
    left: 70px;
    background: linear-gradient(135deg, var(--green-deep) 0%, var(--green-dark) 45%, var(--green-light) 100%);
    display: flex;
    align-items: center;
    justify-content: center;
  }
  .brand {
    display: flex;
    align-items: center;
    gap: 14px;
    font-family: "Roboto", Arial, sans-serif;
    font-weight: 700;
  }
  .brand__mark {
    width: 26px;
    height: 26px;
    border-radius: 50%;
  }
  .card--front .brand { color: #1d6f2c; font-size: 46px; }
  .card--front .brand__mark { background: #1d6f2c; }
  .card--back {
    left: 630px;
    background: var(--paper);
  }
  .card--back .brand {
    position: absolute;
    left: 34px;
    top: 120px;
    color: var(--green-mid);
    font-size: 40px;
  }
  .card--back .brand__mark { background: var(--green-mid); width: 30px; height: 30px; }
  .details {
    position: absolute;
    left: 262px;
    top: 36px;
    width: 220px;
    color: var(--ink);
    font-size: 12.5px;
    line-height: 1.4;
  }
  .details__name {
    font-family: "Fjalla One", "Arial Narrow", sans-serif;
    color: var(--green-dark);
    font-size: 18px;
    line-height: 1.15;
  }
  .details__title { font-size: 12.5px; margin-bottom: 6px; }
  .details__rule { height: 1.5px; background: var(--green-mid); margin-bottom: 12px; }
  .details__address { margin-bottom: 12px; }
  .contact { list-style: none; }
  .contact li { display: flex; align-items: center; gap: 8px; }
  .contact svg { width: 11px; height: 11px; fill: var(--green-mid); flex: none; }
</style>
</head>
<body>
  <section class="card card--front" aria-label="Card front">
    <div class="brand"><span class="brand__mark"></span>Quorvel</div>
  </section>

  <section class="card card--back" aria-label="Card back">
    <div class="brand"><span class="brand__mark"></span>Quorvel</div>
    <div class="details">
      <h1 class="details__name">Marcus Delvecki, MBA</h1>
      <p class="details__title">Executive Director</p>
      <div class="details__rule"></div>
      <p class="details__address">48315 Brackwell Avenue, Suite 512<br>Richmond Hill, ON, L7R 5K2</p>
      <ul class="contact">
        <li><svg viewBox="0 0 12 12"><path d="M2.5 1 L4.5 1 L5 3.5 L3.8 4.5 Q4.8 6.8 7.5 8.2 L8.5 7 L11 7.5 L11 9.5 Q10.5 11 9 11 Q1 10 1 2.5 Q1 1 2.5 1Z"/></svg>905-362-7048, Ext. 218</li>
        <li><svg viewBox="0 0 12 12"><path d="M3.5 0.5 H8.5 Q9.5 0.5 9.5 1.5 V10.5 Q9.5 11.5 8.5 11.5 H3.5 Q2.5 11.5 2.5 10.5 V1.5 Q2.5 0.5 3.5 0.5Z M3.5 1.8 V9.2 H8.5 V1.8Z"/></svg>416-573-2046</li>
        <li><svg viewBox="0 0 12 12"><path d="M0.5 2.5 H11.5 V9.5 H0.5Z M1.2 3 L6 6.6 L10.8 3Z" fill-rule="evenodd"/></svg>marcus@quorvel.ca</li>
        <li><svg viewBox="0 0 12 12"><circle cx="6" cy="6" r="5.5"/><path d="M0.5 6 H11.5 M6 0.5 V11.5" stroke="#f8f8f6" stroke-width="0.9"/></svg>www.quorvel.ca</li>
      </ul>
    </div>
  </section>
</body>
</html>
```